FACEBOOK PAGE FOR QUILLON PLUMBING GROUP

We need a facebook banner for our new plumbing business.

Needs to be catchy and inline with our logo.

Phone: 0491 726 384
Email: hello@quillon.com.au
website: www.quillon.com.au
Servicing: Perth Metro Areas and surrounding suburbs
Services:
*We offer a wide range of services, including:
Plumbing – General maintenance, blocked drains, toilet repairs, burst pipes, reticulation, renovations & emergencies.

*Hot Water – Installation, servicing & repairs for all systems.

*Cooling & Heating – Air conditioning, evaporative cooling & heater servicing.

*Filtration – Filtered taps, under-sink systems & whole-house filtration setups.

Our Mission

Quillon Group believes plumbing shouldn't break the bank - or your trust. Our mission is to provide honest, affordable, and no-nonsense plumbing services that get the job done right the first time. No runaround - just reliable work, and the respect every customer deserves.

What Makes Us Different???

Upfront Fixed Pricing
No surprises, no hidden fees. You get clear, honest quotes before any work begins.

Respectful, Customer-First Service
We show up on time, communicate clearly, and treat your property like it’s our own.

Locals Serving Locals
We’re proud to support the Perth community with reliable, high-quality plumbing backed by real local care.

FOR THE DESIGNER A little background on us as a new biz for your reference:
By Locals, For Locals
After 13 years in the plumbing industry, seasoned local plumber Marcus founded his company to address the widespread issue of homeowners and businesses being overcharged or receiving inferior work. He knew there had to be a better way—and that’s when Quillon was created.
Today, Quillon Group is a trusted plumbing company based in Osborne Park, proudly serving residential, commercial, and industrial clients across the Perth metro area. With over a decade of experience, we deliver expert workmanship, fair pricing, and treat every job—big or small—with the same care and professionalism.
Need it done right—and affordably? Sort it with QUILLON today!

```html
<!DOCTYPE html>
<html lang="en">
<head>
<meta charset="utf-8">
<title>Quillon Trades Group – Facebook Banner</title>
<link rel="stylesheet" href="https://fonts.googleapis.com/css2?family=Figtree:wght@400;500;700;800&display=swap">
<style>
  :root {
    --stage: #383837;
    --paper: #ffffff;
    --navy: #27235c;
    --deep-blue: #0b4a85;
    --sky: #1d9edb;
    --bright: #1aa3e4;
    --ink: #1f1d3f;
  }
  * { margin: 0; padding: 0; box-sizing: border-box; }
  html, body { width: 1200px; height: 762px; overflow: hidden; background: var(--stage); }
  body { font-family: "Figtree", sans-serif; color: var(--ink); position: relative; }

  .banner { position: absolute; left: 124px; top: 131px; width: 913px; height: 515px; background: var(--paper); overflow: hidden; }

  .brand { position: absolute; left: 32px; top: 54px; width: 290px; color: var(--navy); font-weight: 800; }
  .brand-name { font-size: 46px; line-height: 52px; letter-spacing: 8px; white-space: nowrap; }
  .brand-sub { font-size: 16px; letter-spacing: 11.5px; margin-top: 10px; white-space: nowrap; }

  .services { position: absolute; left: 32px; top: 0; }
  .service { position: absolute; left: 0; width: 320px; }
  .service-icon { position: absolute; left: 0; width: 36px; height: 44px; }
  .service-title { position: absolute; left: 43px; top: 0; font-size: 27px; font-weight: 500; color: var(--navy); white-space: nowrap; line-height: 32px; }
  .service-desc { position: absolute; left: 43px; top: 32px; font-size: 9.5px; line-height: 12px; color: var(--ink); white-space: nowrap; }

  .hero { position: absolute; left: 355px; top: 0; width: 558px; height: 224px; }
  .hero-text { position: absolute; left: 470px; top: 30px; color: #fff; font-weight: 800; font-size: 44px; line-height: 58px; letter-spacing: -0.4px; white-space: nowrap; }

  .about { position: absolute; left: 411px; top: 228px; width: 500px; }
  .heading { position: absolute; font-size: 26px; font-weight: 500; color: var(--navy); white-space: nowrap; line-height: 30px; }
  .heading::before { content: ""; position: absolute; left: -18px; top: 12px; width: 9px; height: 9px; background: linear-gradient(135deg, var(--sky), var(--navy)); transform: rotate(45deg); }
  .mission-quote { position: absolute; left: 0; top: 31px; font-size: 14px; line-height: 18.5px; width: 500px; color: var(--ink); }
  .points { position: absolute; left: 0; top: 103px; list-style: none; }
  .point { position: absolute; left: 0; width: 480px; font-size: 12.5px; line-height: 16px; white-space: nowrap; }
  .point svg { position: absolute; left: 0; top: 2px; width: 12px; height: 12px; }
  .point span { display: block; padding-left: 21px; }

  .footer { position: absolute; left: 0; top: 442px; width: 913px; height: 73px; background: linear-gradient(90deg, #163f85 0%, var(--navy) 30%, var(--navy) 100%); }
  .contact-bar { position: absolute; left: 72px; top: 0; width: 769px; height: 44px; }
  .contact { position: absolute; top: 0; height: 44px; display: flex; align-items: center; color: #fff; font-size: 22px; white-space: nowrap; }
  .contact svg { width: 29px; height: 29px; margin-right: 7px; flex: none; }
  .contact.phone { font-weight: 700; }
</style>
</head>
<body>
<main class="banner">

  <div class="brand">
    <div class="brand-name">QUILLON</div>
    <div class="brand-sub">TRADES GROUP</div>
  </div>

  <section class="services">
    <div class="service" style="top:152px">
      <svg class="service-icon" viewBox="0 0 36 44" style="top:0" fill="none" stroke="#27235c" stroke-width="1.6">
        <path d="M22 4h8M26 4v6M20 10h12v10H20zM20 14h-8a6 6 0 0 0-6 6v6M3 26h6v4H3z"/>
        <path d="M6 36c-2 3-2 5 0 6 2-1 2-3 0-6z" stroke="#1d9edb"/>
      </svg>
      <div class="service-title">Plumbing</div>
      <div class="service-desc">General maintenance, blocked drains,<br>toilet repairs, burst pipes, reticulation,<br>renovations &amp; emergencies.</div>
    </div>
    <div class="service" style="top:226px">
      <svg class="service-icon" viewBox="0 0 36 44" style="top:-2px" fill="none" stroke="#27235c" stroke-width="1.6">
        <rect x="2" y="12" width="32" height="22" rx="2"/>
        <path d="M2 19h32M28 12V4M8 24h4M15 26h14M15 30h14"/>
        <circle cx="9" cy="28" r="2"/>
      </svg>
      <div class="service-title" style="left:41px">Hot Water</div>
      <div class="service-desc" style="left:41px">Installation, servicing &amp; repairs<br>for all systems.</div>
    </div>
    <div class="service" style="top:295px">
      <svg class="service-icon" viewBox="0 0 36 50" style="top:3px;height:50px" fill="none" stroke="#27235c" stroke-width="1.8">
        <rect x="3" y="2" width="30" height="38" rx="3"/>
        <path d="M18 10c-2 3-2 5 0 6 2-1 2-3 0-6zM12 30a6 6 0 0 1 12 0M18 30l-2-3M9 40v6h5v-6M22 40v6h5v-6"/>
      </svg>
      <div class="service-title" style="left:41px">Cooling &amp; Heating</div>
      <div class="service-desc" style="left:41px">Air conditioning, evaporative<br>cooling &amp; heater servicing.</div>
    </div>
    <div class="service" style="top:363px">
      <svg class="service-icon" viewBox="0 0 36 44" style="top:3px" fill="none" stroke="#27235c" stroke-width="1.6">
        <path d="M2 34V6h12M4 4h10v6H4M14 10h14a4 4 0 0 1 4 4v2h-6H14M2 34h6V16"/>
        <path d="M26 22l-1 2 1 2-1 2M29 22l-1 2 1 2-1 2M32 22l-1 2 1 2-1 2"/>
      </svg>
      <div class="service-title" style="left:37px">Filtration</div>
      <div class="service-desc" style="left:37px">Filtered taps, under-sink systems &amp;<br>whole-house filtration setups.</div>
    </div>
  </section>

  <svg class="hero" viewBox="0 0 558 224" preserveAspectRatio="none">
    <defs>
      <linearGradient id="heroFill" x1="0" x2="1" y1="0" y2="0">
        <stop offset="0.25" stop-color="#1d9edb"/>
        <stop offset="0.62" stop-color="#0b4a85"/>
        <stop offset="1" stop-color="#0b4a85"/>
      </linearGradient>
    </defs>
    <path d="M66 0H558V222H70L13 136Q2 118 11 93Z" fill="#27235c"/>
    <path d="M68 0H558V218H74L19 134Q9 118 16 95Z" fill="url(#heroFill)"/>
    <rect x="70" y="218" width="488" height="4" fill="#1aa3e4"/>
  </svg>
  <h1 class="hero-text">Need it done right-<br>and affordably?<br>Fix it with QUILLON.</h1>

  <section class="about">
    <h2 class="heading" style="left:17px;top:2px">Our Mission</h2>
    <p class="mission-quote">"Plumbing shouldn't break the bank — or your trust. We provide honest, affordable, no-nonsense services that get it right the first time."</p>
    <h2 class="heading" style="left:20px;top:70px">What Makes Us Different</h2>
    <ul class="points">
      <li class="point" style="top:0">
        <svg viewBox="0 0 12 12" fill="none" stroke="#1d9edb" stroke-width="1.2"><circle cx="6" cy="6" r="5"/><path d="M3.5 6l2 2 4-5" stroke="#27235c"/></svg>
        <span>Upfront Fixed Pricing<br>No hidden fees. Know your cost before we start.</span>
      </li>
      <li class="point" style="top:37px">
        <svg viewBox="0 0 12 12" fill="none" stroke="#1d9edb" stroke-width="1.2"><circle cx="6" cy="6" r="5"/><path d="M3.5 6l2 2 4-5" stroke="#27235c"/></svg>
        <span>Respectful, Customer-First Service<br>We show up on time &amp; treat your space like our own.</span>
      </li>
      <li class="point" style="top:73px">
        <svg viewBox="0 0 12 12" fill="none" stroke="#1d9edb" stroke-width="1.2"><circle cx="6" cy="6" r="5"/><path d="M3.5 6l2 2 4-5" stroke="#27235c"/></svg>
        <span>Locals Serving Locals<br>Proudly Perth-based — real service from real locals.</span>
      </li>
    </ul>
  </section>

  <footer class="footer">
    <svg class="contact-bar" viewBox="0 0 769 44" preserveAspectRatio="none">
      <defs>
        <linearGradient id="barFill" x1="0" x2="1">
          <stop offset="0" stop-color="#1d9edb"/>
          <stop offset="0.5" stop-color="#1a66ad"/>
          <stop offset="1" stop-color="#1d9edb"/>
        </linearGradient>
      </defs>
      <path d="M18 0H751L769 22 751 44H18L0 22Z" fill="url(#barFill)"/>
    </svg>
    <div class="contact phone" style="left:102px">
      <svg viewBox="0 0 30 30"><circle cx="15" cy="15" r="14" fill="#0b4a85"/><path d="M11 8l3 4-2 2q2 4 5 5l2-2 4 3-2 3q-9-1-12-12z" fill="none" stroke="#fff" stroke-width="1.6"/></svg>
      0491 726 384
    </div>
    <div class="contact" style="left:299px">
      <svg viewBox="0 0 30 30" fill="none" stroke="#fff" stroke-width="1.3"><circle cx="15" cy="15" r="14" fill="#0b4a85" stroke="none"/><circle cx="15" cy="15" r="9"/><ellipse cx="15" cy="15" rx="4" ry="9"/><path d="M6 15h18M8 10h14M8 20h14"/></svg>
      www.quillon.com.au
    </div>
    <div class="contact" style="left:555px">
      <svg viewBox="0 0 30 30" fill="none" stroke="#fff" stroke-width="1.5"><circle cx="15" cy="15" r="14" fill="#0b4a85" stroke="none"/><rect x="7" y="10" width="16" height="11"/><path d="M7 10l8 7 8-7"/></svg>
      hello@quillon.com.au
    </div>
  </footer>

</main>
</body>
</html>
```